Powerpoint and Word Document Template

Our target market are C-suite executives in banks, credit unions, non-bank financial institutions, financial technology companies and in the law firms, private equity firms and the like that are also advising the industry.

design should convey: confidence, trust, expertise, experience, value, advice, relationship focus.

For the stationery design, we will need the .doc format as well.

Industry/Entity Type

Consulting

Font styles to use
Sans Serif

Colors
0356a4
3277b5
85acd3
cedeed
eaf1f7
ffffff

Requirements
Must have
• must use the logo and color scheme included in the attached zip file. must include a powerpoint template with a cover slide, section break slides, slides for images/graphics, slides for side by side content, and slides for regular content.

Note: this should also include designs for word documents like stationary and envelopes based on the same concept.

```html
<!DOCTYPE html>
<html lang="en">
<head>
<meta charset="utf-8">
<title>Veltora Advisory – Presentation Template Overview</title>
<link href="https://fonts.googleapis.com/css2?family=Montserrat:wght@500;600;700;800&family=Poppins:wght@400;500;600;700&display=swap" rel="stylesheet">
<style>
:root{
  --stage:#474747;
  --scroll:#2e2e2e;
  --navy:#1c3361;
  --blue:#0356a4;
  --mid:#3277b5;
  --sky:#85acd3;
  --pale:#cedeed;
  --mist:#eaf1f7;
  --white:#ffffff;
  --ink:#1c2a44;
}
*{margin:0;padding:0;box-sizing:border-box}
html,body{width:1200px;height:731px;overflow:hidden;background:var(--stage)}
body{position:relative;font-family:"Poppins",Arial,sans-serif;color:var(--ink)}

.scrollbar{position:absolute;right:0;top:0;width:14px;height:731px;background:var(--scroll)}
.scrollbar-thumb{position:absolute;left:3px;top:332px;width:8px;height:16px;background:#9a9a9a;border-radius:2px}

.slide{position:absolute;width:360px;height:202.5px;overflow:hidden;background:var(--white);outline:1px solid #6a6a6a}
.col-1{left:24px}.col-2{left:414px}.col-3{left:804px}
.row-1{top:28px}.row-2{top:261px}.row-3{top:493px}
.abs{position:absolute}

.brand{position:absolute;display:flex;align-items:center;gap:2.5px;font-family:"Montserrat",sans-serif;font-weight:700;font-size:5.2px;letter-spacing:.4px;color:var(--navy);white-space:nowrap}
.brand-mark{width:6px;height:6px;border:1px solid currentColor}
.brand.on-dark{color:var(--white)}
.brand.large{font-size:7.5px;gap:3.5px}
.brand.large .brand-mark{width:9px;height:9px;border-width:1.3px}

.copy{font-size:3.2px;line-height:1.35;color:var(--ink)}
.copy.light{color:#dfe8f3}
.sub{font-family:"Montserrat",sans-serif;font-weight:700;font-size:4.6px;color:var(--blue);line-height:1.2}
.sub.big{font-size:6px}
.sub.white{color:var(--white)}

.slide-head{position:absolute;left:0;top:0;width:100%;height:17px;background:var(--mid)}
.slide-head-title{position:absolute;left:12px;top:5px;font-family:"Montserrat",sans-serif;font-weight:700;font-size:6.3px;letter-spacing:1px;color:var(--white)}
.slide-head .brand{right:10px;top:5.5px;color:var(--white)}

.foot-rule{position:absolute;left:10px;top:189px;width:205px;height:.6px;background:#9aa7b8}
.foot-caption{position:absolute;left:10px;top:192px;font-family:"Montserrat",sans-serif;font-weight:700;font-size:3px;letter-spacing:.2px;color:var(--navy);white-space:nowrap}
.foot-caption.on-dark{color:var(--white)}
.page-no{position:absolute;right:6px;bottom:5px;width:13px;height:13px;background:var(--mid);color:var(--white);font-family:"Montserrat",sans-serif;font-weight:700;font-size:4.5px;display:flex;align-items:center;justify-content:center}

.panel-navy{position:absolute;background:var(--navy)}
.panel-pale{position:absolute;background:var(--pale)}
.panel-mist{position:absolute;background:#dce8f4}

/* Chart slide */
.chart-title{position:absolute;left:17px;top:8px;font-family:"Montserrat",sans-serif;font-weight:800;font-size:10.5px;color:var(--navy)}
.chart-rule{position:absolute;left:17px;right:12px;top:23px;height:.6px;background:var(--sky)}
.key-point{position:absolute;left:42px;display:flex;gap:4px;align-items:flex-start}
.key-dot{width:5px;height:5px;background:var(--blue);margin-top:.5px;flex:none}
.key-dot.soft{background:var(--sky)}
.key-text{font-size:3.6px;font-weight:600;line-height:1.3;color:var(--blue);width:70px}
.key-text.soft{color:var(--sky)}
.kpi{position:absolute;left:12px;top:98px;width:106px;height:31px;background:#dfe9f4;display:flex;align-items:center;gap:5px;padding-left:8px}
.kpi-value{font-family:"Montserrat",sans-serif;font-weight:800;font-size:9px;color:var(--navy);line-height:1}
.kpi-note{font-size:2.8px;color:var(--navy);margin-top:1px;line-height:1.2}
.caption-band{position:absolute;left:0;top:150px;width:100%;height:52.5px;background:var(--navy)}

/* Photo areas */
.photo{position:absolute}
.photo-office{background:linear-gradient(120deg,#eef1f5 0%,#cfd7e2 40%,#8f9fb8 75%,#4f6a97 100%)}
.photo-hourglass{background:radial-gradient(ellipse at 55% 40%,#6a86ad 0%,#3f5d8c 45%,#22406e 100%)}
.photo-desk{background:radial-gradient(ellipse at 40% 60%,#3a78c0 0%,#2361a8 45%,#16407e 100%)}
.overlay-blue{position:absolute;background:rgba(50,119,181,.78)}
.hero-title{position:absolute;font-family:"Montserrat",sans-serif;font-weight:700;color:var(--white)}

.contact-bar{position:absolute;left:0;top:168px;width:100%;height:34.5px;display:flex;align-items:center;padding:0 16px;gap:9px}
.contact-bar.soft{background:rgba(133,172,211,.88)}
.contact-bar.deep{background:rgba(22,49,96,.88)}
.contact{display:flex;align-items:center;gap:3px;font-family:"Montserrat",sans-serif;font-weight:700;font-size:3.5px;color:var(--white);line-height:1.25;white-space:nowrap}
.contact svg{width:9px;height:9px;flex:none}
.contact-divider{width:.6px;height:12px;background:rgba(255,255,255,.7)}
.contact.web{margin-left:auto}

/* Lists */
.service-item{position:absolute;left:237px;display:flex;gap:6px;width:110px}
.service-item svg{width:8px;height:8px;flex:none;margin-top:1px}
.service-item .sub{font-size:4.2px;margin-bottom:1px}
.step{position:absolute;left:260px;width:88px}
.step .sub{font-size:4.3px;margin-bottom:.8px}
.ticks{list-style:none}
.ticks li{position:relative;padding-left:5px;font-size:3.2px;line-height:1.35;margin-bottom:1.4px}
.ticks li::before{content:"";position:absolute;left:0;top:1px;border-left:2.5px solid var(--navy);border-top:1.5px solid transparent;border-bottom:1.5px solid transparent}
.num-list{list-style:none;font-size:3.2px;line-height:1.35}
</style>
</head>
<body>

<!-- Row 1 -->
<section class="slide col-1 row-1" style="background:#f6f9fc">
  <div class="chart-title">Image/Graphic Title_</div>
  <div class="brand" style="right:12px;top:10px"><span class="brand-mark"></span>VELTORA</div>
  <div class="chart-rule"></div>
  <div class="key-point" style="top:41px"><span class="key-dot"></span><span class="key-text">Lorem ipsum dolor sit amet, consectetuer adipiscing elit.</span></div>
  <div class="key-point" style="top:63px"><span class="key-dot soft"></span><span class="key-text soft">Lorem ipsum dolor sit amet, consectetuer adipiscing elit.</span></div>
  <div class="kpi">
    <svg width="16" height="16" viewBox="0 0 16 16"><circle cx="8" cy="8" r="7" fill="none" stroke="#1c3361" stroke-width="1.2"/><path d="M8 12V4M4.8 7.2L8 4l3.2 3.2" fill="none" stroke="#1c3361" stroke-width="1.2"/></svg>
    <div><div class="kpi-value">25% Y/Y</div><div class="kpi-note">Lorem ipsum dolor sit amet,<br>consectetuer adipiscing elit.</div></div>
  </div>
  <svg class="abs" style="left:0;top:0" width="360" height="150" viewBox="0 0 360 150" font-family="Poppins, sans-serif" font-size="4" fill="#1c3361">
    <g stroke="#dbe4ef" stroke-width=".4">
      <line x1="160" y1="43" x2="328" y2="43"/><line x1="160" y1="58.2" x2="328" y2="58.2"/><line x1="160" y1="73.4" x2="328" y2="73.4"/><line x1="160" y1="88.6" x2="328" y2="88.6"/><line x1="160" y1="103.8" x2="328" y2="103.8"/>
    </g>
    <line x1="160" y1="119" x2="328" y2="119" stroke="#1c3361" stroke-width=".6"/>
    <g text-anchor="end"><text x="154" y="120.5">0</text><text x="154" y="105.3">200</text><text x="154" y="90.1">400</text><text x="154" y="74.9">600</text><text x="154" y="59.7">800</text><text x="154" y="44.5">1000</text></g>
    <g text-anchor="middle"><text x="164" y="128.5">100</text><text x="181.8" y="128.5">200</text><text x="199.6" y="128.5">300</text><text x="217.4" y="128.5">400</text><text x="235.2" y="128.5">500</text><text x="253" y="128.5">600</text><text x="270.8" y="128.5">700</text><text x="288.6" y="128.5">800</text><text x="306.4" y="128.5">900</text><text x="324.2" y="128.5">1000</text></g>
    <polyline fill="none" stroke="#85acd3" stroke-width=".9" points="164,96.2 181.8,96.2 199.6,65.8 217.4,119 235.2,81 253,81 270.8,111.4 288.6,111.4 306.4,111.4 324.2,96.2"/>
    <polyline fill="none" stroke="#1c3361" stroke-width=".9" points="164,111.4 181.8,119 199.6,96.2 217.4,111.4 235.2,96.2 253,96.2 270.8,96.2 288.6,65.8 306.4,111.4 324.2,43"/>
    <g fill="#85acd3"><circle cx="164" cy="96.2" r="1"/><circle cx="181.8" cy="96.2" r="1"/><circle cx="199.6" cy="65.8" r="1"/><circle cx="217.4" cy="119" r="1"/><circle cx="235.2" cy="81" r="1"/><circle cx="253" cy="81" r="1"/><circle cx="270.8" cy="111.4" r="1"/><circle cx="288.6" cy="111.4" r="1"/><circle cx="306.4" cy="111.4" r="1"/><circle cx="324.2" cy="96.2" r="1"/></g>
    <g fill="#1c3361"><circle cx="164" cy="111.4" r="1"/><circle cx="181.8" cy="119" r="1"/><circle cx="199.6" cy="96.2" r="1"/><circle cx="217.4" cy="111.4" r="1"/><circle cx="235.2" cy="96.2" r="1"/><circle cx="253" cy="96.2" r="1"/><circle cx="270.8" cy="96.2" r="1"/><circle cx="288.6" cy="65.8" r="1"/><circle cx="306.4" cy="111.4" r="1"/><circle cx="324.2" cy="43" r="1"/></g>
  </svg>
  <div class="caption-band"></div>
  <p class="copy light abs" style="left:16px;top:157px;width:76px">Lorem ipsum dolor sit amet, consectetuer adipiscing elit, sed diam nonummy nibh euismod tincidunt ut laoreet dolore magna aliquam erat volutpat.</p>
  <p class="copy light abs" style="left:100px;top:157px;width:76px">Lorem ipsum dolor sit amet, consectetuer adipiscing elit, sed diam nonummy nibh euismod tincidunt ut laoreet dolore magna aliquam erat volutpat.</p>
  <p class="copy light abs" style="left:184px;top:157px;width:76px">Lorem ipsum dolor sit amet, consectetuer adipiscing elit, sed diam nonummy nibh euismod tincidunt ut laoreet dolore magna aliquam erat volutpat.</p>
  <div class="brand on-dark large" style="right:14px;top:160px"><span class="brand-mark"></span>VELTORA</div>
  <div class="foot-caption on-dark" style="left:16px;top:193px">IMAGE/GRAPHICS SECTION // FULL IMAGE/GRAPHICS SLIDE WITH CAPTIONS</div>
  <div class="page-no">04</div>
</section>

<section class="slide col-2 row-1" style="background:var(--navy)">
  <div class="photo photo-office" role="img" aria-label="Photo of two consultants reviewing documents at an office desk" style="left:95px;top:0;width:265px;height:189px"></div>
  <div class="overlay-blue" style="left:245px;top:0;width:115px;height:189px"></div>
  <svg class="abs" style="left:0;top:0" width="360" height="203" viewBox="0 0 360 203"><polygon points="88,189 88,120 150,189" fill="#1c3361"/><polygon points="0,189 360,189 360,202.5 0,202.5" fill="#1c3361"/><rect x="100" y="185" width="260" height="4" fill="#0356a4"/></svg>
  <div class="brand on-dark large" style="left:10px;top:11px"><span class="brand-mark"></span>VELTORA</div>
  <div class="hero-title" style="left:268px;top:60px;font-size:13px;line-height:1.2">Image/<br>Graphic<br>Title_</div>
  <p class="copy light abs" style="left:10px;top:126px;width:72px">Lorem ipsum dolor sit amet, consectetuer adipiscing elit, sed diam nonummy nibh euismod.</p>
  <p class="copy light abs" style="left:10px;top:150px;width:72px">Ut wisi enim ad minim veniam, quis nostrud exerci tation ullamcorper suscipit lobortis.</p>
  <div class="page-no" style="left:6px;right:auto">05</div>
  <div class="foot-caption on-dark" style="left:190px;top:193px">IMAGE/GRAPHICS SECTION // 1/2 IMAGE/GRAPHICS SLIDE WITH CAPTIONS</div>
</section>

<section class="slide col-3 row-1">
  <div class="photo photo-hourglass" role="img" aria-label="Photo of an hourglass standing on pebbles, tinted blue" style="left:0;top:0;width:360px;height:202.5px"></div>
  <div class="brand on-dark large" style="left:20px;top:16px"><span class="brand-mark"></span>VELTORA</div>
  <div class="hero-title" style="left:232px;top:89px;font-size:15px;letter-spacing:3px">BREAK</div>
  <div class="contact-bar soft">
    <div class="contact"><svg viewBox="0 0 10 10"><rect x=".5" y=".5" width="9" height="9" fill="none" stroke="#fff" stroke-width=".6"/><path d="M5 8.2S2.6 5.6 2.6 4.1a2.4 2.4 0 0 1 4.8 0C7.4 5.6 5 8.2 5 8.2z" fill="#fff"/></svg><span>42 Harbor Lane<br>01234 Riverton, NC</span></div>
    <span class="contact-divider"></span>
    <div class="contact"><svg viewBox="0 0 10 10"><rect x=".5" y=".5" width="9" height="9" fill="none" stroke="#fff" stroke-width=".6"/><rect x="2" y="3" width="6" height="4.2" fill="none" stroke="#fff" stroke-width=".6"/><path d="M2 3l3 2.3L8 3" fill="none" stroke="#fff" stroke-width=".6"/></svg><span>info@veltoraadvisory.com</span></div>
    <span class="contact-divider"></span>
    <div class="contact"><svg viewBox="0 0 10 10"><path d="M2.5 2h1.6l.7 1.8-1 .8a5 5 0 0 0 1.8 1.8l.8-1 1.8.7V7.7A1 1 0 0 1 7 8.5 5.5 5.5 0 0 1 1.5 3a1 1 0 0 1 1-1z" fill="#fff"/></svg><span>+1 (555) 010 2040</span></div>
    <div class="contact web">VELTORAADVISORY.COM</div>
  </div>
</section>

<!-- Row 2 -->
<section class="slide col-1 row-2">
  <header class="slide-head"><div class="slide-head-title">THE SLIDE TITLE</div><div class="brand"><span class="brand-mark"></span>VELTORA</div></header>
  <svg class="abs" style="left:0;top:0" width="220" height="190" viewBox="0 0 220 190" font-family="Montserrat, sans-serif" font-weight="700" font-size="4" text-anchor="middle">
    <g stroke="#1c3361" stroke-width=".5" stroke-dasharray="1 1" fill="none">
      <path d="M70 80 Q85 100 110 119"/><path d="M110 81 L110 106"/><path d="M149 80 Q135 100 110 119"/><path d="M66 102 Q90 110 97 119"/><path d="M154 102 Q130 110 123 119"/>
    </g>
    <g fill="#fff" stroke="#0356a4" stroke-width="1.4">
      <polygon points="70,51 83,58.5 83,73.5 70,81 57,73.5 57,58.5"/>
      <polygon points="110,51 123,58.5 123,73.5 110,81 97,73.5 97,58.5"/>
      <polygon points="149,51 162,58.5 162,73.5 149,81 136,73.5 136,58.5"/>
    </g>
    <g fill="#fff" stroke="#1c3361" stroke-width="1.4">
      <polygon points="51,87 64,94.5 64,109.5 51,117 38,109.5 38,94.5"/>
      <polygon points="169,87 182,94.5 182,109.5 169,117 156,109.5 156,94.5"/>
    </g>
    <g fill="#0356a4"><circle cx="70" cy="62" r="2"/><circle cx="110" cy="62" r="2"/><circle cx="149" cy="62" r="2"/></g>
    <g fill="#1c3361"><circle cx="51" cy="98" r="2"/><circle cx="169" cy="98" r="2"/></g>
    <g fill="#1c3361"><text x="70" y="71">Risk Mgt</text><text x="110" y="71">Research</text><text x="149" y="71">Forensics</text><text x="51" y="107">Strategy</text><text x="169" y="107">Control</text></g>
    <circle cx="110" cy="119" r="12" fill="#0356a4"/>
    <rect x="104.5" y="114" width="11" height="10" rx="1" fill="none" stroke="#fff" stroke-width=".9"/><line x1="104.5" y1="117" x2="115.5" y2="117" stroke="#fff" stroke-width=".9"/>
    <text x="110" y="145" font-size="6" fill="#1c3361">Our Financial Advisory</text>
    <text x="110" y="151" font-size="3.2" font-weight="500" fill="#1c2a44">Lorem ipsum dolor sit amet consectetuer</text>
    <text x="110" y="155" font-size="3.2" font-weight="500" fill="#1c2a44">adipiscing elit.</text>
  </svg>
  <div class="panel-navy" style="left:220px;top:17px;width:140px;height:185.5px"></div>
  <svg class="abs" style="left:220px;top:150px" width="140" height="52" viewBox="0 0 140 52"><path d="M40 52 L58 20 L76 52" fill="none" stroke="#3277b5" stroke-width="6" opacity=".45"/></svg>
  <div class="service-item" style="top:31px"><svg viewBox="0 0 8 8"><circle cx="4" cy="3.3" r="2.4" fill="none" stroke="#fff" stroke-width=".6"/><rect x="3" y="6" width="2" height="1.5" fill="#fff"/></svg><div><div class="sub white">Strategy.</div><p class="copy light">Lorem ipsum dolor sit amet consectetuer adipiscing elit, sed diam nonummy nibh euismod tincidunt.</p></div></div>
  <div class="service-item" style="top:61px"><svg viewBox="0 0 8 8"><path d="M4 1v6M2.5 2.5h3M1 5a3 3 0 0 0 6 0" fill="none" stroke="#fff" stroke-width=".6"/></svg><div><div class="sub white">Risk Management.</div><p class="copy light">Lorem ipsum dolor sit amet consectetuer adipiscing elit, sed diam nonummy nibh euismod tincidunt.</p></div></div>
  <div class="service-item" style="top:91px"><svg viewBox="0 0 8 8"><path d="M3 1h2v2.5l2 3.5H1l2-3.5z" fill="none" stroke="#fff" stroke-width=".6"/></svg><div><div class="sub white">Research.</div><p class="copy light">Lorem ipsum dolor sit amet consectetuer adipiscing elit, sed diam nonummy nibh euismod tincidunt.</p></div></div>
  <div class="service-item" style="top:121px"><svg viewBox="0 0 8 8"><circle cx="4.8" cy="3.2" r="2.2" fill="none" stroke="#fff" stroke-width=".6"/><path d="M3.2 4.8L1 7" stroke="#fff" stroke-width=".8"/></svg><div><div class="sub white">Forensic Audit.</div><p class="copy light">Lorem ipsum dolor sit amet consectetuer adipiscing elit, sed diam nonummy nibh euismod tincidunt.</p></div></div>
  <div class="service-item" style="top:151px"><svg viewBox="0 0 8 8"><path d="M2.5 1.5h3L5 3a2.8 2.8 0 1 1-2 0z" fill="#fff"/></svg><div><div class="sub white">Control.</div><p class="copy light">Lorem ipsum dolor sit amet consectetuer adipiscing elit, sed diam nonummy nibh euismod tincidunt.</p></div></div>
  <div class="foot-rule"></div>
  <div class="foot-caption">SIDE-BY-SIDE SECTION // 2-COLUMN SIDE-BY-SIDE SLIDE (GOLDEN RATIO)</div>
  <div class="page-no">09</div>
</section>

<section class="slide col-2 row-2">
  <header class="slide-head"><div class="slide-head-title">THE SLIDE TITLE</div><div class="brand"><span class="brand-mark"></span>VELTORA</div></header>
  <div class="panel-mist" style="left:120px;top:17px;width:120px;height:185.5px"></div>
  <div class="panel-navy" style="left:240px;top:17px;width:120px;height:185.5px"></div>
  <svg class="abs" style="left:240px;top:150px" width="120" height="52" viewBox="0 0 120 52"><path d="M10 52 L28 22 L46 52" fill="none" stroke="#3277b5" stroke-width="6" opacity=".45"/></svg>
  <div class="abs" style="left:20px;top:26px;width:92px">
    <div class="sub big" style="margin-bottom:4px">Lorem ipsum dolor elit sit amet.</div>
    <p class="copy" style="margin-bottom:4px">Consectetuer elit adipiscing, sed diam nonummy ex nibh. Euismod tincidunt ut laoreet dolore magna aliquam erat. Exerci ullamcorper suscipit lobortis nisl ut nonummy aliquip commodo.</p>
    <ul class="ticks">
      <li>Lorem ipsum dolor sit amet laoreet aliquam ullamcorper</li>
      <li>Consecr elit adipsim sed diam nonummy exea</li>
      <li>Euismod tincidunt ut laoreet dolore sit adipiscing</li>
      <li>Magna aliquam erat nibh ex commodo laoreet</li>
      <li>Exerci tation ullamcorper suscipit lobortis diam</li>
    </ul>
  </div>
  <div class="step" style="top:27px"><div class="sub white">Step 01</div><p class="copy light">Lorem ipsum dolor sit amet oculite mejee, consectetuer adipiscing elit, sed diam nonummy nibh euismod.</p></div>
  <div class="step" style="top:59px"><div class="sub white">Step 02</div><p class="copy light">Lorem ipsum dolor sit amet oculite mejee, consectetuer adipiscing elit, sed diam nonummy nibh euismod.</p></div>
  <div class="step" style="top:91px"><div class="sub white">Step 03</div><p class="copy light">Lorem ipsum dolor sit amet oculite mejee, consectetuer adipiscing elit, sed diam nonummy nibh euismod.</p></div>
  <div class="step" style="top:123px"><div class="sub white">Step 04</div><p class="copy light">Lorem ipsum dolor sit amet oculite mejee, consectetuer adipiscing elit, sed diam nonummy nibh euismod.</p></div>
  <div class="step" style="top:155px"><div class="sub white">Step 05</div><p class="copy light">Lorem ipsum dolor sit amet oculite mejee, consectetuer adipiscing elit, sed diam nonummy nibh euismod.</p></div>
  <div class="foot-rule" style="width:180px"></div>
  <div class="foot-caption">SIDE-BY-SIDE SECTION // 3-COLUMN SIDE-BY-SIDE SLIDE (EQUAL RATIO)</div>
  <div class="page-no">10</div>
</section>

<section class="slide col-3 row-2">
  <header class="slide-head"><div class="slide-head-title">THE SLIDE TITLE</div><div class="brand"><span class="brand-mark"></span>VELTORA</div></header>
  <div class="panel-navy" style="left:21px;top:28px;width:117px;height:45px"></div>
  <div class="panel-navy" style="left:21px;top:79px;width:117px;height:45px"></div>
  <div class="panel-navy" style="left:21px;top:130px;width:117px;height:45px"></div>
  <div class="abs" style="left:27px;top:34px;width:30px;height:33px;background:var(--mist)"></div>
  <div class="abs" style="left:27px;top:85px;width:30px;height:33px;background:var(--mist)"></div>
  <div class="abs" style="left:27px;top:136px;width:30px;height:33px;background:var(--mist)"></div>
  <div class="abs" style="left:63px;top:34px;width:70px"><div class="sub white" style="font-size:4.3px">Step 02</div><p class="copy light">Lorem ipsum dolor sit amet oculite mejee, consectetuer adipiscing elit, sed diam nonummy nibh euismod tincidunt ut laoreet dolore magna aliquam erat.</p></div>
  <div class="abs" style="left:63px;top:85px;width:70px"><div class="sub white" style="font-size:4.3px">Step 02</div><p class="copy light">Lorem ipsum dolor sit amet oculite mejee, consectetuer adipiscing elit, sed diam nonummy nibh euismod tincidunt ut laoreet dolore magna aliquam erat.</p></div>
  <div class="abs" style="left:63px;top:136px;width:70px"><div class="sub white" style="font-size:4.3px">Step 02</div><p class="copy light">Lorem ipsum dolor sit amet oculite mejee, consectetuer adipiscing elit, sed diam nonummy nibh euismod tincidunt ut laoreet dolore magna aliquam erat.</p></div>

  <div class="abs" style="left:147px;top:28px;width:42px;height:45px;background:var(--mist)"></div>
  <div class="sub abs" style="left:196px;top:28px">Here is a much longer subtitle.</div>
  <p class="copy abs" style="left:196px;top:35px;width:68px">Lorem ipsum dolor sit amet oculite mejee, consectetuer adipiscing elit. Sed diam nonummy nibh euismod tincidunt ut laoreet dolore magna aliquam erat. Consectetuer ad adipiscing elit, lorem ipsum dolor sit amet.</p>
  <p class="copy abs" style="left:271px;top:28px;width:68px">Oculite mejee, sed diam nonummy nibh euismod tincidunt ut laoreet dolore magna aliquam erat. Sed diam nonummy nibh euismod. Consectetuer ad adipiscing elit, sed diam nonummy nibh euismod tincidunt.</p>

  <div class="sub abs" style="left:197px;top:79px">Here is a much longer subtitle.</div>
  <p class="copy abs" style="left:147px;top:82px;width:45px">Lorem ipsum dolor sit amet oculite mejee, consectetuer adipiscing elit. Sed diam nonummy nibh euismod tincidunt ut laoreet dolore.</p>
  <p class="copy abs" style="left:197px;top:86px;width:68px">Lorem ipsum dolor sit amet oculite mejee, consectetuer adipiscing elit. Sed diam nonummy nibh euismod tincidunt ut laoreet dolore magna aliquam erat.</p>
  <div class="abs" style="left:272px;top:84px;width:68px;height:37px;background:var(--mist)"></div>

  <div class="abs" style="left:147px;top:130px;width:42px;height:45px;background:var(--mist)"></div>
  <div class="sub abs" style="left:196px;top:130px">Here is a much longer subtitle.</div>
  <p class="copy abs" style="left:196px;top:137px;width:68px">Lorem ipsum dolor sit amet oculite mejee, consectetuer adipiscing elit. Sed diam nonummy nibh euismod tincidunt ut laoreet dolore magna aliquam erat. Consectetuer ad adipiscing elit.</p>
  <p class="copy abs" style="left:271px;top:130px;width:68px">Oculite mejee, sed diam nonummy nibh euismod tincidunt ut laoreet dolore magna aliquam erat. Sed diam nonummy nibh euismod. Consectetuer ad adipiscing elit, sed diam nonummy nibh.</p>
  <div class="foot-rule" style="width:180px"></div>
  <div class="foot-caption">REGULAR CONTENT SECTION // 3X3 GRID REGULAR SLIDE (GOLDEN RATIO)</div>
  <div class="page-no">16</div>
</section>

<!-- Row 3 -->
<section class="slide col-1 row-3">
  <header class="slide-head"><div class="slide-head-title">THE SLIDE TITLE</div><div class="brand"><span class="brand-mark"></span>VELTORA</div></header>
  <div class="panel-navy" style="left:21px;top:30px;width:58px;height:69px"></div>
  <div class="abs" style="left:86px;top:30px;width:34px;height:69px;background:var(--sky)"></div>
  <div class="abs" style="left:123px;top:30px;width:56px"><div class="sub">Subtitle One.</div><p class="copy">Lorem ipsum dolor ego ulit amet eud orduite du meje, consectetuer diam adipiscing elit, sed ipsum meta diam nonummy nibhit euismod tincidunt ut laoreet dolore magna aliquam erat. Lorem ipsum dolor sit amet, sed diam nonummy nibh euismod.</p></div>
  <div class="abs" style="left:185px;top:30px;width:154px;height:45px;background:var(--sky)"></div>
  <div class="panel-navy" style="left:21px;top:107px;width:58px;height:69px"></div>
  <div class="abs" style="left:86px;top:107px;width:56px"><div class="sub">Subtitle One.</div><p class="copy">Lorem ipsum dolor ego ulit amet eud orduite du meje, consectetuer diam adipiscing elit, sed ipsum meta diam nonummy nibhit euismod tincidunt ut laoreet dolore magna aliquam erat. Lorem ipsum dolor sit amet eud orduite du meje.</p></div>
  <div class="abs" style="left:145px;top:107px;width:33px;height:69px;background:var(--sky)"></div>
  <div class="sub abs" style="left:185px;top:107px;width:160px;font-size:5px">Lorem ipsum dolor sit amet eula eusimod nibh.</div>
  <div class="abs" style="left:185px;top:115px;width:68px"><p class="copy" style="margin-bottom:2px">Consectetuer elit adipiscing, sed diam nonummy ex nibh. Euismod tincidunt ut laoreet dolore magna aliquam erat.</p><ol class="num-list"><li>1. Exerci tation ullamcorper suscipit lobortis nisl ut aliquip ex ea commodo.</li><li>2. Consectetuer elit adipiscing, sed diam nonummy ex nibh.</li><li>1. Exerci tation ullamcorper suscipit lobortis nisl.</li></ol></div>
  <div class="abs" style="left:270px;top:115px;width:68px"><ol class="num-list" style="margin-bottom:2px"><li>2. Lorem ipsum dolor sit ullamcorper suscipit</li><li>3. Euismod tincidunt ut laoreet dolore magna aliquam.</li></ol><p class="copy">Consectetuer elit adipiscing, sed diam nonummy ex nibh. Euismod tincidunt ut laoreet dolore magna aliquam erat. Consectetuer elit adipiscing, sed diam nonummy ex nibh.</p></div>
  <div class="foot-rule" style="width:180px"></div>
  <div class="foot-caption">REGULAR CONTENT SECTION // 3X3 GRID REGULAR SLIDE (GOLDEN RATIO)</div>
  <div class="page-no">14</div>
</section>

<section class="slide col-2 row-3">
  <header class="slide-head"><div class="slide-head-title">THE SLIDE TITLE</div><div class="brand"><span class="brand-mark"></span>VELTORA</div></header>
  <!-- left half -->
  <div class="panel-pale" style="left:21px;top:30px;width:43px;height:45px"></div>
  <div class="sub abs" style="left:68px;top:30px">Subtitle One.</div>
  <p class="copy abs" style="left:68px;top:36px;width:52px">Lorem ipsum dolor edoeit amet eude orduite meje, consectetuer adipiscing elit, sed ipsum meta diam nonummy nibhit euismod tincidunt ut laoreet dolore magna aliquam erat.</p>
  <p class="copy abs" style="left:124px;top:30px;width:52px">Consectetuer ad adipiscing elit, lorem ipsum dolor sit amet, sed ipsum meta diam nonummy nibhit euismod tincidunt ut laoreet dolore magna aliquam erat nibh.</p>
  <div class="sub abs" style="left:78px;top:80px">Subtitle One.</div>
  <p class="copy abs" style="left:21px;top:86px;width:52px">Lorem ipsum dolor edoeit amet eude orduite meje, consectetuer adipiscing elit, sed ipsum meta diam nonummy nibhit euismod tincidunt ut laoreet dolore magna aliquam erat.</p>
  <p class="copy abs" style="left:78px;top:86px;width:50px">Consectetuer ad adipiscing elit, lorem ipsum dolor sit amet, sed ipsum meta diam nonummy nibhit euismod tincidunt ut laoreet dolore magna.</p>
  <div class="panel-pale" style="left:132px;top:80px;width:43px;height:45px"></div>
  <div class="panel-pale" style="left:21px;top:130px;width:43px;height:45px"></div>
  <div class="sub abs" style="left:68px;top:130px">Subtitle One.</div>
  <p class="copy abs" style="left:68px;top:136px;width:52px">Lorem ipsum dolor edoeit amet eude orduite meje, consectetuer adipiscing elit, sed ipsum meta diam nonummy nibhit euismod tincidunt ut laoreet dolore magna aliquam erat.</p>
  <p class="copy abs" style="left:124px;top:130px;width:52px">Consectetuer ad adipiscing elit, lorem ipsum dolor sit amet, sed ipsum meta diam nonummy nibhit euismod tincidunt ut laoreet dolore magna aliquam erat nibh.</p>
  <!-- right half -->
  <div class="panel-pale" style="left:185px;top:30px;width:43px;height:45px"></div>
  <div class="sub abs" style="left:232px;top:30px">Subtitle One.</div>
  <p class="copy abs" style="left:232px;top:36px;width:52px">Lorem ipsum dolor edoeit amet eude orduite meje, consectetuer adipiscing elit, sed ipsum meta diam nonummy nibhit euismod tincidunt ut laoreet dolore magna aliquam erat.</p>
  <p class="copy abs" style="left:288px;top:30px;width:52px">Consectetuer ad adipiscing elit, lorem ipsum dolor sit amet, sed ipsum meta diam nonummy nibhit euismod tincidunt ut laoreet dolore magna aliquam erat nibh.</p>
  <div class="sub abs" style="left:242px;top:80px">Subtitle One.</div>
  <p class="copy abs" style="left:185px;top:86px;width:52px">Lorem ipsum dolor edoeit amet eude orduite meje, consectetuer adipiscing elit, sed ipsum meta diam nonummy nibhit euismod tincidunt ut laoreet dolore magna aliquam erat.</p>
  <p class="copy abs" style="left:242px;top:86px;width:50px">Consectetuer ad adipiscing elit, lorem ipsum dolor sit amet, sed ipsum meta diam nonummy nibhit euismod tincidunt ut laoreet dolore magna.</p>
  <div class="panel-pale" style="left:296px;top:80px;width:43px;height:45px"></div>
  <div class="panel-pale" style="left:185px;top:130px;width:43px;height:45px"></div>
  <div class="sub abs" style="left:232px;top:130px">Subtitle One.</div>
  <p class="copy abs" style="left:232px;top:136px;width:52px">Lorem ipsum dolor edoeit amet eude orduite meje, consectetuer adipiscing elit, sed ipsum meta diam nonummy nibhit euismod tincidunt ut laoreet dolore magna aliquam erat.</p>
  <p class="copy abs" style="left:288px;top:130px;width:52px">Consectetuer ad adipiscing elit, lorem ipsum dolor sit amet, sed ipsum meta diam nonummy nibhit euismod tincidunt ut laoreet dolore magna aliquam erat nibh.</p>
  <div class="foot-rule" style="width:180px"></div>
  <div class="foot-caption">REGULAR CONTENT SECTION // 2X3 GRID REGULAR SLIDE (EQUAL RATIO)</div>
  <div class="page-no">15</div>
</section>

<section class="slide col-3 row-3">
  <div class="photo photo-desk" role="img" aria-label="Photo of a hand writing notes beside a laptop, tinted blue" style="left:0;top:0;width:360px;height:202.5px"></div>
  <div class="brand on-dark large" style="left:20px;top:16px"><span class="brand-mark"></span>VELTORA</div>
  <div class="hero-title" style="left:0;width:100%;text-align:center;top:91px;font-size:14px;letter-spacing:2px">THANK YOU</div>
  <div class="contact-bar deep">
    <div class="contact"><svg viewBox="0 0 10 10"><rect x=".5" y=".5" width="9" height="9" fill="none" stroke="#fff" stroke-width=".6"/><path d="M5 8.2S2.6 5.6 2.6 4.1a2.4 2.4 0 0 1 4.8 0C7.4 5.6 5 8.2 5 8.2z" fill="#fff"/></svg><span>42 Harbor Lane<br>01234 Riverton, NC</span></div>
    <span class="contact-divider"></span>
    <div class="contact"><svg viewBox="0 0 10 10"><rect x=".5" y=".5" width="9" height="9" fill="none" stroke="#fff" stroke-width=".6"/><rect x="2" y="3" width="6" height="4.2" fill="none" stroke="#fff" stroke-width=".6"/><path d="M2 3l3 2.3L8 3" fill="none" stroke="#fff" stroke-width=".6"/></svg><span>info@veltoraadvisory.com</span></div>
    <span class="contact-divider"></span>
    <div class="contact"><svg viewBox="0 0 10 10"><path d="M2.5 2h1.6l.7 1.8-1 .8a5 5 0 0 0 1.8 1.8l.8-1 1.8.7V7.7A1 1 0 0 1 7 8.5 5.5 5.5 0 0 1 1.5 3a1 1 0 0 1 1-1z" fill="#fff"/></svg><span>+1 (555) 010 2040</span></div>
    <div class="contact web">VELTORAADVISORY.COM</div>
  </div>
</section>

<div class="scrollbar"><div class="scrollbar-thumb"></div></div>
</body>
</html>
```